Tenth Annual Silverfern Ivory Carnival Soiree to Benefit Tidewell Ledger Circle Foundation

Date: 2 February 2024
Location: The Halcrest Pelican Shoals Coral Bay Resort & Spa
Time: Doors open 5:00pm
Attire: White Elegance (a variety of masks will be available at the extravaganza)

Target Market(s)

Early to mid career men and women (aged 25-40)

Industry/Entity Type

Financial Services / Asset Management

Font styles to use
Serif

Colors
0054AA
0677BA
7BADD7
CADEEF
E8F1F8
00AB8E
00BBA5
67D7C9
C6EFE9
E9F9F6
59FF00
82FF00
B8FF75
E3FFCB
F4FFEA

Requirements
Must have
• Masquerade images. The event is being held on the beach in the Caribbean.

```html
<!DOCTYPE html>
<html lang="en">
<head>
<meta charset="utf-8">
<title>Silverfern Ivory Carnival Soiree</title>
<link href="https://fonts.googleapis.com/css2?family=Poppins:wght@100;200;300;400;500;700;800&family=Oswald:wght@500;700&family=Anton&family=Playball&display=swap" rel="stylesheet">
<style>
  :root {
    --stage: #6d6768;
    --ink: #231f20;
    --slate: #4a4d53;
    --gold-dark: #8a6535;
    --gold: #a57a45;
    --gold-light: #d9b47e;
    --brand-navy: #2b3990;
    --white: #ffffff;
    --mist-1: #f4f4f3;
    --mist-2: #dcdedf;
  }
  * { box-sizing: border-box; margin: 0; padding: 0; }
  html, body { width: 1200px; height: 2400px; overflow: hidden; }
  body { background: var(--stage); position: relative; font-family: "Poppins", sans-serif; color: var(--ink); }

  .poster {
    position: absolute; left: 50px; top: 488px; width: 1100px; height: 1423px;
    overflow: hidden; box-shadow: 0 20px 40px rgba(0,0,0,.35);
  }
  .poster__backdrop {
    position: absolute; inset: 0;
    background:
      radial-gradient(ellipse 420px 520px at 900px 760px, #8d9094 0%, #c9cbcd 45%, rgba(220,222,223,0) 75%),
      radial-gradient(ellipse 700px 500px at 300px 1250px, #ffffff 0%, rgba(255,255,255,0) 70%),
      linear-gradient(160deg, var(--mist-1) 0%, var(--mist-2) 40%, #eef0f0 70%, #f7f7f7 100%);
  }

  .brand { position: absolute; left: 92px; top: 92px; display: flex; align-items: center; gap: 18px; }
  .brand__dot { width: 64px; height: 64px; border-radius: 50%; background: var(--brand-navy); }
  .brand__name { font-weight: 500; font-size: 30px; color: var(--brand-navy); line-height: 1; }

  .presents { position: absolute; left: 98px; top: 212px; font-size: 26px; letter-spacing: 12px; font-weight: 400; }

  .edition { position: absolute; left: 80px; top: 230px; font-family: "Playball", cursive; line-height: 1; }
  .edition__num { font-size: 200px; color: var(--ink); }
  .edition__suffix { font-size: 110px; color: #6c6f73; margin-left: -6px; }

  .title-kicker {
    position: absolute; left: 84px; top: 416px; font-size: 52px; line-height: 1;
    font-weight: 300; letter-spacing: -1.5px; color: var(--ink); white-space: nowrap;
  }

  .title-main {
    position: absolute; left: 80px; top: 475px; font-family: "Anton", sans-serif; font-size: 211px; line-height: 1;
    letter-spacing: 2px; font-weight: 400;
    background: linear-gradient(90deg, var(--gold-dark) 0%, var(--gold-light) 45%, var(--gold) 75%, var(--gold-dark) 100%);
    -webkit-background-clip: text; background-clip: text; color: transparent;
  }
  .title-script {
    position: absolute; left: 92px; top: 648px; font-family: "Playball", cursive; font-size: 112px; line-height: 1;
    color: var(--gold-dark); -webkit-text-stroke: 2px var(--white); paint-order: stroke fill;
  }
  .title-tail { position: absolute; left: 74px; top: 720px; font-size: 190px; font-weight: 100; line-height: 1; color: var(--gold); letter-spacing: -6px; }

  .date { position: absolute; left: 84px; top: 940px; display: flex; align-items: flex-end; line-height: 1; }
  .date__day { font-size: 150px; font-weight: 800; letter-spacing: -6px; margin-bottom: -14px; }
  .date__stack { display: flex; flex-direction: column; margin-left: 4px; }
  .date__ord { font-size: 78px; font-weight: 200; margin-bottom: -6px; }
  .date__month { font-size: 72px; font-weight: 700; color: var(--gold); letter-spacing: -1px; }
  .date__year { font-size: 72px; font-weight: 500; color: var(--ink); }

  .time-bar { position: absolute; left: 84px; top: 1097px; width: 690px; height: 56px; background: var(--slate); color: var(--white); font-size: 42px; font-weight: 400; letter-spacing: 2px; line-height: 58px; padding-left: 16px; }

  .venue { position: absolute; left: 84px; top: 1172px; display: flex; gap: 10px; font-size: 34px; line-height: 1.05; color: #4a4a4a; }
  .venue__pin { width: 26px; height: 34px; margin-top: 8px; flex: none; }
  .venue strong { font-weight: 700; color: var(--ink); }

  .attire { position: absolute; left: 90px; top: 1270px; width: 940px; height: 76px; display: flex; }
  .attire__label { width: 206px; background: var(--ink); color: var(--white); font-weight: 700; font-size: 44px; display: flex; align-items: center; justify-content: center; letter-spacing: 1px; }
  .attire__body { flex: 1; background: var(--gold); display: flex; align-items: center; padding-left: 18px; gap: 18px; color: var(--white); }
  .attire__value { font-family: "Oswald", sans-serif; font-weight: 500; font-size: 48px; letter-spacing: -1px; }
  .attire__note { font-size: 23px; line-height: 1.15; font-weight: 400; }
</style>
</head>
<body>
  <main class="poster">
    <div class="poster__backdrop" role="img" aria-label="Photograph of a silver glitter masquerade mask resting on soft white feathers"></div>

    <div class="brand">
      <span class="brand__dot"></span>
      <span class="brand__name">Tidewell Ledger Circle</span>
    </div>

    <p class="presents">Presents</p>

    <p class="edition"><span class="edition__num">10</span><span class="edition__suffix">th</span></p>

    <p class="title-kicker">ANNUAL SILVERFERN</p>
    <h1 class="title-main">IVORY</h1>
    <p class="title-script">Carnival</p>
    <p class="title-tail">SOIREE</p>

    <div class="date">
      <span class="date__day">2</span>
      <span class="date__stack">
        <span class="date__ord">ND</span>
        <span><span class="date__month">FEBRUARY</span><span class="date__year">2024</span></span>
      </span>
    </div>

    <div class="time-bar">TIME: DOORS OPEN 5:00PM</div>

    <div class="venue">
      <svg class="venue__pin" viewBox="0 0 26 34" aria-hidden="true">
        <path d="M13 1C6.4 1 1 6.2 1 12.6 1 21 13 33 13 33s12-12 12-20.4C25 6.2 19.6 1 13 1z" fill="#8a6535"/>
        <circle cx="13" cy="12.5" r="5" fill="#f2f2f2"/>
      </svg>
      <p><strong>The Halcrest Pelican Shoals</strong> Coral Bay<br>Resort &amp; Spa</p>
    </div>

    <div class="attire">
      <div class="attire__label">ATTIRE</div>
      <div class="attire__body">
        <span class="attire__value">WHITE ELEGANCE</span>
        <span class="attire__note">(a variety of masks will be<br>available at the extravaganza)</span>
      </div>
    </div>
  </main>
</body>
</html>
```